Personal Signature

Hi, im Tomás Quiroga Benítez, im 25 years old, I just graduated of civil engineer. Im Mexican and Spanish and I would like your help designing my personal signature that im using my entire life. I would like a simple and modern Signature.

Civil Engineer

```html
<!DOCTYPE html>
<html lang="es">
<head>
<meta charset="utf-8">
<title>Tomás Quiroga Benítez — Firma personal</title>
<link rel="stylesheet" href="https://fonts.googleapis.com/css2?family=Kaushan+Script&display=swap">
<style>
  :root {
    --canvas-bg: #e6e6e6;
    --navy-deep: #0f0d24;
    --navy: #16163a;
    --navy-light: #22244e;
    --ink-white: #ffffff;
  }
  html, body {
    margin: 0;
    padding: 0;
    width: 1200px;
    height: 1200px;
    overflow: hidden;
    background: var(--canvas-bg);
  }
  .signature-card {
    position: absolute;
    left: 50px;
    top: 211px;
    width: 1100px;
    height: 778px;
    overflow: hidden;
    background: var(--navy);
  }
  .backdrop-photo {
    position: absolute;
    inset: 0;
    background:
      radial-gradient(ellipse 30% 36% at 28% 42%, var(--navy-deep) 0%, rgba(15,13,36,0) 100%),
      radial-gradient(ellipse 34% 26% at 78% 72%, var(--navy-light) 0%, rgba(34,36,78,0) 100%),
      linear-gradient(160deg, var(--navy) 0%, #1a1a42 55%, var(--navy) 100%);
  }
  .signature-name {
    position: absolute;
    left: 0;
    right: 0;
    top: 318px;
    margin: 0;
    text-align: center;
    font-family: "Kaushan Script", cursive;
    font-weight: 400;
    font-size: 94px;
    line-height: 1;
    color: var(--ink-white);
    letter-spacing: 0;
  }
  .signature-swash {
    position: absolute;
    left: 0;
    top: 0;
    width: 1100px;
    height: 778px;
  }
</style>
</head>
<body>
  <main class="signature-card">
    <div class="backdrop-photo" role="img" aria-label="Darkened navy photo of a construction hard hat, rolled blueprints and a calculator on engineering plans"></div>
    <h1 class="signature-name">Tomás Quiroga Benítez</h1>
    <svg class="signature-swash" viewBox="0 0 1100 778" aria-hidden="true">
      <path d="M589 495 C 640 440, 760 440, 941 453" fill="none" stroke="var(--ink-white)" stroke-width="2.2" stroke-linecap="round"/>
    </svg>
  </main>
</body>
</html>
```